Corporate Dinner Invitation – Bold, Professional Look with Subtle Arabic Flair

We are seeking a bold, professional invitation design for a VIP dinner event hosted by Torlan during the KQRW Summit on Friday, July 18th. This will be used primarily for LinkedIn promotion and as a PDF invitation shared directly with physicians, so it must look clean and polished in portrait orientation.
The design should reflect a high-end corporate aesthetic while still being eye-catching. We’d like to see a very subtle Arabic or Moroccan-inspired design element — think minimal patterns or shapes worked lightly into the background or border. This flair should feel tasteful and restrained, not thematic or decorative. If you need some inspiration for the arabic/morrocan theme - please look up the Zafrani Lounge website (https://www.zafranilo.com/).
Design Guidelines:
Portrait orientation only
Bold, clean, modern layout
Use of both Torlan and ORB Spine TQ brand colors preferred
Use of both Torlan and ORB Spine TQ logos (ORB Spine TQ logo is a subsidiary of the Torlan logo - so please make the Torlan logo the larger of the two; they are both the same company - Torlan owns ORB Spine TQ).
Strong, readable typography that looks professional and commands attention
Design must work well as both a LinkedIn graphic and a standalone PDF
Visual tone: corporate, high-level, medical, innovative
Event Details:
Date: Friday, July 18th
Time: 8:00pm - 10:00pm EST
Location: Zafrani Lounge (817 SE W Canal Rd, Miami, FL 33145)
Speakers: Gregory Lasko, MD; Calvin Brandt, MD; Suren Pathak, MD (I am including headshots of each speaker - they need to be included on the invite - please remove the backgrounds in the headshot to make all of them uniform looking on the invite)
Final Deliverables:
High-res PDF
PNG or JPEG preview for LinkedIn
Editable source file (Canva, AI or InDesign)
Target Market(s)
Physicians
Industry/Entity Type
Medical Device

```html
<!DOCTYPE html>
<html lang="en">
<head>
<meta charset="utf-8">
<title>VIP Dinner Invitation – Torlan</title>
<link rel="stylesheet" href="https://fonts.googleapis.com/css2?family=Cinzel:wght@400;500;600;700&display=swap">
<style>
  :root {
    --maroon: #45141f;
    --wine: #4a1622;
    --blush: #f5e8e8;
    --blush-edge: #b98b93;
    --suit-blue: #5d6f9c;
    --suit-shirt: #d9a9b0;
    --coat-white: #e9e9ee;
    --coat-shade: #c9c9d2;
    --brand-green: #6db33f;
    --brand-purple: #a4287f;
  }
  * { margin: 0; padding: 0; box-sizing: border-box; }
  html, body { width: 846px; height: 1200px; overflow: hidden; background: var(--maroon); }
  .invite {
    position: relative;
    width: 846px;
    height: 1200px;
    background: var(--maroon);
    font-family: "Cinzel", serif;
    color: var(--wine);
  }
  .panel {
    position: absolute;
    left: 70px;
    top: 60px;
    width: 704px;
    height: 1075px;
    background: var(--blush);
    border: 1px solid var(--blush-edge);
    text-align: center;
    overflow: hidden;
  }
  .title-vip,
  .title-dinner {
    position: absolute;
    left: 0;
    right: 0;
    font-weight: 400;
    line-height: 1;
    font-size: 68px;
    letter-spacing: 1px;
  }
  .title-vip { top: 88px; }
  .title-dinner { top: 171px; }
  .details {
    position: absolute;
    left: 0;
    right: 0;
    top: 258px;
    font-size: 26px;
    font-weight: 600;
    line-height: 30.5px;
    letter-spacing: 0.5px;
  }
  .speakers {
    position: absolute;
    left: 0;
    right: 0;
    top: 426px;
    font-weight: 600;
  }
  .speakers-label { font-size: 15px; letter-spacing: 0.5px; }
  .speakers-names { font-size: 17px; margin-top: 3px; letter-spacing: 0.5px; }
  .speaker-photos {
    position: absolute;
    left: 0;
    top: 555px;
    width: 702px;
    height: 405px;
  }
  .headshot {
    position: absolute;
    bottom: 0;
    border-radius: 130px 130px 0 0;
    -webkit-mask-image: linear-gradient(180deg, #000 70%, transparent 100%);
    mask-image: linear-gradient(180deg, #000 70%, transparent 100%);
  }
  .headshot-lasko {
    left: 0;
    width: 306px;
    height: 396px;
    z-index: 3;
    background: linear-gradient(90deg, var(--suit-blue) 0%, var(--suit-blue) 35%, var(--suit-shirt) 50%, var(--suit-blue) 65%, var(--suit-blue) 100%);
  }
  .headshot-brandt {
    left: 290px;
    width: 232px;
    height: 400px;
    z-index: 2;
    background: linear-gradient(90deg, var(--coat-shade) 0%, var(--coat-white) 40%, var(--coat-white) 100%);
  }
  .headshot-pathak {
    left: 430px;
    width: 272px;
    height: 400px;
    z-index: 1;
    background: linear-gradient(90deg, var(--coat-white) 0%, var(--coat-shade) 50%, var(--coat-white) 100%);
  }
  .brands {
    position: absolute;
    left: 0;
    right: 0;
    top: 1000px;
    display: flex;
    justify-content: center;
    align-items: baseline;
    gap: 22px;
    font-weight: 600;
  }
  .brand-primary { font-size: 32px; color: var(--brand-green); }
  .brand-secondary { font-size: 20px; color: var(--brand-purple); }
</style>
</head>
<body>
  <main class="invite">
    <section class="panel">
      <h1 class="title">
        <span class="title-vip">VIP</span>
        <span class="title-dinner">DINNER</span>
      </h1>
      <div class="details">
        <p>Friday, July 18th</p>
        <p>8:00pm - 10:00pm EST</p>
        <p>at Zafrani Lounge</p>
        <p>817 SE W Canal Rd, Miami, FL 33145</p>
      </div>
      <div class="speakers">
        <p class="speakers-label">Speakers:</p>
        <p class="speakers-names">Gregory Lasko, MD | Calvin Brandt, MD | Suren Pathak, MD</p>
      </div>
      <div class="speaker-photos">
        <div class="headshot headshot-pathak" role="img" aria-label="Headshot of Suren Pathak, MD, in a white coat, background removed"></div>
        <div class="headshot headshot-brandt" role="img" aria-label="Headshot of Calvin Brandt, MD, in a white coat, background removed"></div>
        <div class="headshot headshot-lasko" role="img" aria-label="Headshot of Gregory Lasko, MD, in a blue blazer, background removed"></div>
      </div>
      <div class="brands">
        <span class="brand-primary">Torlan</span>
        <span class="brand-secondary">ORB Spine TQ</span>
      </div>
    </section>
  </main>
</body>
</html>
```